Business Card for new Overseas Property Buying Business

Hi

We need a new business card for our new business.

We are Faraway Nest Finders. So we search locations on behalf of our clients to find them the ideal home.

These are mainly holiday homes in nice locations - but sometimes people are looking to relocate.

I am looking for a nice simple design - that has some class and professionalism about it. Taking inspiration from our logo.

Text wise I was thinking of maybe having something like. (THE FONT FOR THIS SHOULD BE LIKE THE WRITING IN THE ATTACHMENT WITH THE MAP ON IT)

1)
What does your dream house have (tick all that apply):
swimming pool x
private vineyard x
herb garden x
full sized football pitch x

2)
How to buy a home abroad:

Method 1:
1) Scour internet for suitable estate agents
2) Arrange hectic holiday timetable with multiple agents in multiple languages
3) Fly to destination to find property was not as it seemed
4) Feel frustrated and helpless
OR
Method 2:
Contact your expert home hunter (details overleaf) - and leave the hard work to them

The end result should give people confidence that they are dealing with a professional organisation - and feel like they can place their trust in them. I would want it to drive them to either contact us directly or visit the website.

Please include name (Gordon Tramley), position (founder), contact numbers x 2, email address, website (www.quelvatrix-moor.com)

I look forward to seeing your entries.

Reason: Hi Sorry to extend - Xmas has got in the way of my plans. I will be providing feedback. Happy Christmas to you all.

```html
<!DOCTYPE html>
<html lang="en">
<head>
<meta charset="utf-8">
<title>Faraway Nest Finders – Business Card</title>
<link href="https://fonts.googleapis.com/css2?family=Libre+Baskerville&family=Arimo&family=Shadows+Into+Light+Two&display=swap" rel="stylesheet">
<style>
  :root {
    --page: #ffffff;
    --card-brown: #4a3f36;
    --back-brown: #4d4239;
    --copper: #e2572f;
    --copper-light: #f08a5d;
    --panel: #ecebea;
    --ink: #3d3631;
    --chalk: #f3eee8;
    --accent: #ef6a3e;
  }
  * { box-sizing: border-box; margin: 0; padding: 0; }
  html, body { width: 1200px; height: 900px; overflow: hidden; background: var(--page); }
  .canvas { position: relative; width: 1200px; height: 900px; }

  .card { position: absolute; top: 39px; width: 445px; height: 723px; }
  .card--front { left: 121px; background: var(--card-brown); }
  .card--back { left: 652px; background: var(--back-brown); }

  .front-frame {
    position: absolute; inset: 21px;
    background: linear-gradient(180deg, var(--copper) 0%, var(--copper-light) 55%, var(--copper) 100%);
    padding: 8px;
  }
  .front-panel {
    position: relative; width: 100%; height: 100%;
    background: var(--panel);
    font-family: "Arimo", Arial, sans-serif; color: var(--ink);
  }
  .holder-name {
    position: absolute; top: 26px; width: 100%; text-align: center;
    font-family: "Libre Baskerville", Georgia, serif; font-size: 24px; color: var(--copper);
  }
  .holder-role {
    position: absolute; top: 58px; width: 100%; text-align: center;
    font-family: "Libre Baskerville", Georgia, serif; font-size: 17px; color: var(--ink);
  }
  .brand-mark {
    position: absolute; top: 158px; left: 50%; transform: translateX(-50%);
    width: 150px; height: 150px; border-radius: 50%;
    background: var(--copper);
  }
  .brand-name {
    position: absolute; top: 363px; width: 100%; text-align: center;
    font-family: "Libre Baskerville", Georgia, serif; font-size: 31px; color: var(--ink);
  }
  .contact-list { position: absolute; left: 24px; top: 526px; list-style: none; }
  .contact-list li {
    display: flex; align-items: center; gap: 6px;
    font-size: 22px; line-height: 28.5px; color: var(--ink);
  }
  .contact-list svg { width: 24px; height: 22px; flex: none; }

  .back-copy {
    position: absolute; left: 43px; top: 96px; width: 370px;
    font-family: "Shadows Into Light Two", cursive; color: var(--chalk);
    font-size: 17px; line-height: 23px;
  }
  .back-copy h2 { font-weight: normal; color: var(--accent); font-size: 21px; line-height: 28px; }
  .back-copy h3 { font-weight: normal; color: var(--accent); font-size: 17px; }
  .wish-list { list-style: none; margin: 26px 0 22px; }
  .wish-list svg { width: 16px; height: 14px; vertical-align: -1px; margin-left: 4px; }
  .method { margin-top: 20px; }
  .method p { margin: 0; }
  .steps { list-style: none; }
</style>
</head>
<body>
<main class="canvas">
  <section class="card card--front" aria-label="Card front">
    <div class="front-frame">
      <div class="front-panel">
        <p class="holder-name">Gordon Tramley</p>
        <p class="holder-role">founder</p>
        <div class="brand-mark" aria-hidden="true"></div>
        <p class="brand-name">Faraway Nest Finders</p>
        <ul class="contact-list">
          <li><svg viewBox="0 0 24 24" aria-hidden="true"><path fill="#e2572f" d="M6.6 10.8a15 15 0 0 0 6.6 6.6l2.2-2.2c.3-.3.7-.4 1-.2 1.1.4 2.3.6 3.6.6.6 0 1 .4 1 1V20c0 .6-.4 1-1 1A17 17 0 0 1 3 4c0-.6.4-1 1-1h3.5c.6 0 1 .4 1 1 0 1.3.2 2.5.6 3.6.1.3 0 .7-.2 1z"/></svg>158 402 317</li>
          <li><svg viewBox="0 0 24 24" aria-hidden="true"><path fill="#e2572f" d="M6.6 10.8a15 15 0 0 0 6.6 6.6l2.2-2.2c.3-.3.7-.4 1-.2 1.1.4 2.3.6 3.6.6.6 0 1 .4 1 1V20c0 .6-.4 1-1 1A17 17 0 0 1 3 4c0-.6.4-1 1-1h3.5c.6 0 1 .4 1 1 0 1.3.2 2.5.6 3.6.1.3 0 .7-.2 1z"/></svg>534 816 095</li>
          <li><svg viewBox="0 0 24 24" aria-hidden="true"><g fill="none" stroke="#e2572f" stroke-width="2"><circle cx="12" cy="12" r="9.5"/><ellipse cx="12" cy="12" rx="4" ry="9.5"/><path d="M2.5 12h19M4 7h16M4 17h16"/></g></svg>www.quelvatrix-moor.com</li>
          <li><svg viewBox="0 0 24 24" aria-hidden="true"><rect x="2" y="5" width="20" height="14" rx="1.5" fill="#e2572f"/><path d="M3 6l9 7 9-7" fill="none" stroke="#ecebea" stroke-width="1.6"/></svg>info@quelvatrix-moor.com</li>
        </ul>
      </div>
    </div>
  </section>

  <section class="card card--back" aria-label="Card back">
    <div class="back-copy">
      <h2>What does your dream house have</h2>
      <ul class="wish-list">
        <li>swimming pool<svg viewBox="0 0 16 14" aria-hidden="true"><path d="M1 7l5 5 9-11" fill="none" stroke="#ef6a3e" stroke-width="2"/></svg></li>
        <li>private vineyard<svg viewBox="0 0 16 14" aria-hidden="true"><path d="M1 7l5 5 9-11" fill="none" stroke="#ef6a3e" stroke-width="2"/></svg></li>
        <li>herb garden<svg viewBox="0 0 16 14" aria-hidden="true"><path d="M1 7l5 5 9-11" fill="none" stroke="#ef6a3e" stroke-width="2"/></svg></li>
        <li>full sized football pitch<svg viewBox="0 0 16 14" aria-hidden="true"><path d="M1 7l5 5 9-11" fill="none" stroke="#ef6a3e" stroke-width="2"/></svg></li>
      </ul>
      <h2>How to buy a home abroad:</h2>
      <div class="method">
        <h3>Method 1:</h3>
        <ol class="steps">
          <li>1) Scour internet for suitable estate agents</li>
          <li>2) Arrange hectic holiday timetable with multiple agents in multiple languages</li>
          <li>3) Fly to destination to find property was not as it seemed</li>
          <li>4) Feel frustrated and helpless</li>
        </ol>
        <p>OR</p>
      </div>
      <div class="method">
        <h3>Method 2:</h3>
        <p>Contact your expert home hunter (details overleaf) - and leave the hard work to them</p>
      </div>
    </div>
  </section>
</main>
</body>
</html>
```